Post Card Mailer for QUIK PATH PROSPECTS using new logo

We need a post card designed to send through the USA mail service that will go to new prospective clients.

The post card will introduce me and my new company and try to educate them our on company and services.

The goal is for them to call me or email me so I can have a discussion and try to sell our product.

Our product is a name list of individuals that are looking for consulting / help to determine if they qualify for USA social security benefits and then help to manage the process. We sell this name list to law firms that help these individuals.

Our services are better because we have a better less expensive way to identify people via the internet that want help. Our conversion rate is 15%, so every 100 leads a law firm buys the will obtain 15 customers / clients.

Designer on Logo took alot longer than expected. Also there were two projects that needed to combined into one. Which was done yesterday.

Target Market(s)

Law firms

Font styles to use
Serif
Sans Serif
Script

Colors

Designer to choose colors to be used in the design.

Requirements
Must have
• The size of the mailer should be about 6 by 8 inches.
• Two sides.
• Side 1: With our Logo and key messages we want to communicate.
• Side 2: A space to be used by the USA mail services in lower right, my photo and an introduction by me to our company and why they should buy from my company.
Nice to have
• Images that represent what we do, how we help, and our target market.
Should not have
• Poor taste in images that upset people

```html
<!DOCTYPE html>
<html lang="en">
<head>
<meta charset="utf-8">
<title>Quik Path Prospects Postcard Mailer</title>
<link rel="stylesheet" href="https://fonts.googleapis.com/css2?family=Oswald:wght@400;500&family=Lato:wght@400;700&display=swap">
<style>
  :root {
    --blue: #1a6fc4;
    --blue-dark: #125aa3;
    --grey: #8a8b8d;
    --ink: #555a60;
    --paper: #ffffff;
    --backdrop: #d9d9d9;
  }
  * { box-sizing: border-box; margin: 0; padding: 0; }
  html, body { width: 1200px; height: 1200px; overflow: hidden; background: var(--backdrop); }
  .sheet { position: relative; width: 1200px; height: 1200px; }
  .card-slot { position: absolute; left: 220px; width: 760px; height: 567px; }
  .card-slot.front-slot { top: 24px; }
  .card-slot.back-slot { top: 609px; }
  .card {
    position: absolute; left: 0; top: 0; width: 650px; height: 485px;
    background: var(--paper); overflow: hidden;
    transform: scale(1.1692); transform-origin: 0 0;
    box-shadow: 0 2px 6px rgba(0,0,0,.18);
    font-family: "Lato", sans-serif; color: var(--ink);
  }
  .card > svg.backdrop { position: absolute; left: 0; top: 0; }
  .abs { position: absolute; }
  .brand { font-family: "Oswald", sans-serif; font-weight: 500; color: var(--blue); line-height: 1; letter-spacing: 1px; }
  .head { font-family: "Oswald", sans-serif; font-weight: 400; color: var(--blue); text-transform: uppercase; line-height: 1.15; }
  .list { list-style: none; }
  .list li { position: relative; padding-left: 15px; line-height: 1.3; }
  .list li::before {
    content: ""; position: absolute; left: 0; top: .42em; width: 9px; height: 6px;
    background: var(--blue);
    clip-path: polygon(0 25%, 55% 25%, 55% 0, 100% 50%, 55% 100%, 55% 75%, 0 75%);
  }
  .list.reverse li { padding-left: 0; padding-right: 15px; }
  .list.reverse li::before { left: auto; right: 0; transform: scaleX(-1); }
  .list.on-blue li { color: #fff; }
  .list.on-blue li::before { background: #fff; }
  .icon-label { font-size: 12px; color: #fff; text-align: center; width: 100px; }

  /* front */
  .front .brand { left: 17px; top: 20px; font-size: 34px; }
  .front .headline { left: 17px; top: 112px; font-size: 31px; }
  .front .lead-points { left: 17px; top: 163px; width: 330px; font-size: 14px; }
  .front .lead-points li { margin-bottom: 13px; }
  .front .pillar { top: 360px; }
  .front .pillar .head { font-size: 17px; margin-bottom: 5px; }
  .front .pillar .list { font-size: 11.5px; }
  .front .pillar .list li { margin-bottom: 3px; }

  /* back */
  .back .intro-name { left: 138px; top: 50px; font-size: 14px; color: #fff; }
  .back .intro-heading { left: 32px; top: 140px; width: 240px; font-size: 15px; color: #fff; }
  .back .intro-points { left: 18px; top: 188px; width: 235px; font-size: 9.2px; }
  .back .intro-points li { margin-bottom: 8px; }
  .back .closing { left: 18px; top: 404px; width: 200px; font-size: 12px; }
  .back .brand { right: 20px; top: 18px; font-size: 22px; text-align: right; }
  .back .tagline { right: 17px; top: 73px; font-size: 11.5px; text-align: right; width: 260px; }
  .back .test-title { right: 17px; top: 125px; font-size: 13px; }
  .back .test-points { right: 17px; top: 146px; width: 260px; font-size: 9.2px; text-align: right; }
  .back .test-points li { margin-bottom: 2px; }
  .back .mail-box { left: 318px; top: 220px; width: 310px; height: 246px; border: 1px solid #9a9a9a; }
  .back .stamp { position: absolute; right: 10px; top: 8px; width: 85px; height: 85px; border: 1px solid #9a9a9a; }
  .back .return-address { position: absolute; left: 12px; top: 8px; font-size: 9.5px; line-height: 1.55; color: #777; }
  .back .addressee { position: absolute; left: 12px; top: 176px; font-size: 9.5px; color: #777; }
</style>
</head>
<body>
<main class="sheet">

  <!-- Side 1 -->
  <div class="card-slot front-slot">
    <section class="card front" aria-label="Postcard front">
      <svg class="backdrop" width="650" height="485" viewBox="0 0 650 485">
        <defs>
          <linearGradient id="photoTone" x1="0" y1="0" x2="1" y2="1">
            <stop offset="0" stop-color="#8f8a4e"/>
            <stop offset=".45" stop-color="#b79a78"/>
            <stop offset="1" stop-color="#6f86a6"/>
          </linearGradient>
          <linearGradient id="mistTone" x1="0" y1="0" x2="1" y2="0">
            <stop offset="0" stop-color="#f3f5f7" stop-opacity="0"/>
            <stop offset="1" stop-color="#e8ebee"/>
          </linearGradient>
        </defs>
        <rect x="300" y="300" width="350" height="170" fill="url(#mistTone)"/>
        <polygon points="338,0 650,0 650,305 445,305" fill="url(#photoTone)" role="img" aria-label="Photo of a caregiver smiling with an elderly man in a wheelchair outdoors"/>
        <polygon points="596,0 650,0 650,100" fill="var(--grey)"/>
        <line x1="0" y1="298" x2="650" y2="298" stroke="var(--blue)" stroke-width="0"/>
        <rect x="0" y="295" width="430" height="7" fill="var(--blue)"/>
        <line x1="448" y1="330" x2="345" y2="58" stroke="var(--blue)" stroke-width="6"/>
        <polygon points="338,38 330,68 356,60" fill="var(--blue)"/>
        <rect x="0" y="470" width="650" height="15" fill="var(--grey)"/>
        <line x1="238" y1="362" x2="238" y2="452" stroke="#c4c4c4" stroke-width="1"/>
        <line x1="455" y1="362" x2="455" y2="452" stroke="#c4c4c4" stroke-width="1"/>
        <!-- law -->
        <circle cx="71" cy="295" r="50" fill="var(--blue)"/>
        <g fill="#fff">
          <rect x="58" y="258" width="28" height="11" transform="rotate(40 72 263)"/>
          <rect x="70" y="266" width="5" height="26" transform="rotate(-50 72 279)"/>
          <rect x="47" y="290" width="30" height="5"/>
        </g>
        <!-- aim -->
        <circle cx="203" cy="290" r="50" fill="var(--blue)"/>
        <g fill="none" stroke="#fff" stroke-width="3">
          <circle cx="200" cy="278" r="22"/>
          <circle cx="200" cy="278" r="14"/>
          <circle cx="200" cy="278" r="6"/>
          <line x1="200" y1="278" x2="222" y2="256"/>
        </g>
        <!-- technology -->
        <circle cx="335" cy="285" r="52" fill="var(--blue)"/>
        <g fill="none" stroke="#fff" stroke-width="2.2">
          <circle cx="335" cy="270" r="13"/>
          <line x1="330" y1="286" x2="340" y2="286"/>
          <line x1="331" y1="291" x2="339" y2="291"/>
          <line x1="335" y1="248" x2="335" y2="242"/>
          <line x1="315" y1="256" x2="310" y2="252"/>
          <line x1="355" y1="256" x2="360" y2="252"/>
          <line x1="311" y1="272" x2="305" y2="272"/>
          <line x1="359" y1="272" x2="365" y2="272"/>
        </g>
      </svg>

      <div class="abs brand">QUIK PATH<br>PROSPECTS</div>
      <h1 class="abs head headline">Best Leads, Best Price</h1>
      <ul class="abs list lead-points">
        <li>Our high conversation rates lowers your client acquisition cost</li>
        <li>Referrals available</li>
      </ul>

      <div class="abs icon-label" style="left:21px;top:316px;">Law</div>
      <div class="abs icon-label" style="left:153px;top:321px;">Aim</div>
      <div class="abs icon-label" style="left:285px;top:315px;">Technology</div>

      <div class="abs pillar" style="left:17px;width:215px;">
        <h2 class="head">High Volume, Quality Leads</h2>
        <ul class="list">
          <li>50 years of SSD domain knowledge</li>
          <li>Tested technology capabilities</li>
        </ul>
      </div>
      <div class="abs pillar" style="left:255px;width:185px;">
        <h2 class="head">Trusted Partner</h2>
        <ul class="list">
          <li>Reliability, Dependable, Helpful</li>
          <li>Deep business &amp; process acumen</li>
        </ul>
      </div>
      <div class="abs pillar" style="left:490px;width:150px;top:355px;">
        <h2 class="head">EZ to Use</h2>
        <ul class="list">
          <li>Integrate seamlessly into your IT systems</li>
          <li>Tailored campaigns</li>
        </ul>
      </div>
    </section>
  </div>

  <!-- Side 2 -->
  <div class="card-slot back-slot">
    <section class="card back" aria-label="Postcard back">
      <svg class="backdrop" width="650" height="485" viewBox="0 0 650 485">
        <defs>
          <linearGradient id="portraitTone" x1="0" y1="0" x2="0" y2="1">
            <stop offset="0" stop-color="#b9c3cc"/>
            <stop offset="1" stop-color="#5c6670"/>
          </linearGradient>
        </defs>
        <polygon points="0,0 353,0 228,390 0,390" fill="var(--blue)"/>
        <polygon points="0,470 192,470 187,485 0,485" fill="var(--blue)"/>
        <line x1="207" y1="485" x2="333" y2="150" stroke="var(--blue)" stroke-width="6"/>
        <polygon points="340,128 320,152 346,160" fill="var(--blue)"/>
        <circle cx="73" cy="73" r="55" fill="#fff"/>
        <circle cx="73" cy="73" r="51" fill="url(#portraitTone)" role="img" aria-label="Portrait photo of the company president"/>
      </svg>

      <div class="abs head intro-name">Marcus Delvane<br>President, Quik Path Prospects</div>
      <h2 class="abs head intro-heading">I want to personally introduce our company to you!</h2>
      <ul class="abs list on-blue intro-points">
        <li>My team as &gt; 50 years of cumulative SSD experience. We have proven technology that delivers the best leads.</li>
        <li>The timing is right for a new competitor in this industry.</li>
        <li>I had to come out of retirement after 30 years with Northwind Industries, the opportunity is just that great … I love building businesses and partnering with great customers!</li>
        <li>Our business, industry, &amp; technical acumen is unrivaled … and we can do it at a cost than no others can.</li>
      </ul>
      <p class="abs head closing">Let's work together to bring social security disability benefits to those in need and deserving!</p>

      <div class="abs brand">QUIK PATH<br>PROSPECTS</div>
      <p class="abs head tagline">Best leads … best price with high volume &amp; quality capacity … leads from a trusted partner that is EZ to use</p>
      <h3 class="abs head test-title">Test our leads</h3>
      <ul class="abs list reverse test-points">
        <li>Start at 250 or 500 Leads.</li>
        <li>Grow to 1,000 … 3,000 or even 10,000!</li>
        <li>We give the right support to your growth.</li>
      </ul>

      <div class="abs mail-box">
        <address class="return-address" style="font-style:normal;">
          Marcus Delvane, President Quik Path Prospects<br>
          2150 Harbor Ridge Drive, Suite 400<br>
          Dayton Ohio OH 45402<br>
          555-014-2287<br>
          marcus@quikpathprospects.com
        </address>
        <div class="stamp" aria-label="Stamp area"></div>
        <p class="addressee">To: Addressee</p>
      </div>
    </section>
  </div>

</main>
</body>
</html>
```